DRAINWELL HOT WATER CYLINDER STICKER – PRINT LAYOUT

SECTION 1 – HOMEOWNER MAINTENANCE GUIDE (Boxed Section):
πŸ“– Hot Water Cylinder Maintenance
βœ… Monthly: Quick visual check for leaks, rust, or pooling water.
βœ… Every 6 Months: Test your TPR (Temperature & Pressure Relief) valve.
β€’ Lift the lever gently until water flows, then release.
β€’ If it’s blocked or constantly dripping – call us immediately.
βœ… Listen: Popping, banging, or rumbling? Could be sediment build-up.
βœ… Annually: Book a professional service to check anode, thermostat & valves.

SECTION 2 – WARNING SIGNS (Highlight Box or Red Accent):
🚨 Call Us Immediately If You Notice:
β€’ No hot water or inconsistent temperature
β€’ Water leaking from tank or pipes
β€’ Rust-coloured water
β€’ Sudden drop in water pressure

SECTION 3 – CALL TO ACTION (Large & Bold):
πŸ“ž NEED HELP FAST? CALL DRAINWELL FIRST!
πŸ“² PHONE: [0431 258 907] (largest text on sticker)
🌐 [www.drainwell.com.au]

FOOTER (Small Print):
Fully Licensed & Insured | HKTR 62840315 | 24/7 Emergency Service
This guide is for general maintenance only. For all repairs or safety concerns, contact a licensed plumber.

βœ… DESIGN RECOMMENDATIONS
β€’ Size: 27cm long x 10cm wide works well (large enough to read easily when standing).
β€’ Material: Waterproof vinyl with strong adhesive.
β€’ Colors:
o Header & Call-to-Action in your brand colors
o Maintenance guide in a light-shaded box for contrast
o Warning signs section with red accent or icon to grab attention
β€’ Icons: Use βœ… πŸ“– 🚨 πŸ“ž for quick scanning.

```html
<!DOCTYPE html>
<html lang="en">
<head>
<meta charset="utf-8">
<title>Drainwell Hot Water Cylinder Sticker</title>
<link href="https://fonts.googleapis.com/css2?family=Lato:ital,wght@0,400;0,700;0,900;1,400&display=swap" rel="stylesheet">
<style>
  :root {
    --page-bg: #f3f3f3;
    --charcoal: #3a3a3c;
    --white: #ffffff;
    --blue-light: #12b4e4;
    --blue-deep: #0f7fb6;
    --brand-blue: #1a9ad6;
    --title-blue: #1ea5dc;
    --orange-red: #ec4425;
    --orange-mid: #f58a24;
    --orange-yellow: #f9bb1c;
    --guide-bg: #e6e7e9;
    --tick-green: #7ac143;
    --ink: #1c1c1e;
    --footer-ink: #eeeeee;
  }
  html, body {
    margin: 0;
    padding: 0;
    width: 1200px;
    height: 960px;
    overflow: hidden;
    background: var(--page-bg);
  }
  .canvas {
    width: 1200px;
    height: 960px;
    display: flex;
    align-items: center;
    justify-content: center;
  }
  .sticker {
    width: 1120px;
    height: 415px;
    display: block;
    box-shadow: 0 6px 24px rgba(0,0,0,0.18);
    font-family: 'Lato', sans-serif;
  }
  .sticker-bg { fill: var(--charcoal); }
  .brand-name { font-weight: 900; font-size: 84px; fill: var(--white); letter-spacing: 1px; }
  .brand-tagline { font-weight: 400; font-size: 40px; fill: var(--white); }
  .brand-dot { fill: var(--brand-blue); }
  .cta-lead { font-weight: 900; font-size: 45px; fill: var(--white); }
  .cta-phone { font-weight: 900; font-size: 92px; fill: var(--white); }
  .cta-web { font-weight: 700; font-size: 38px; fill: var(--white); }
  .warning-title { font-weight: 900; font-size: 74px; fill: var(--white); }
  .warning-item { font-weight: 700; font-size: 41px; fill: var(--white); }
  .guide-box { fill: var(--guide-bg); stroke: var(--title-blue); stroke-width: 3; }
  .guide-title { font-weight: 900; font-size: 52px; fill: var(--title-blue); }
  .guide-icon { fill: none; stroke: var(--title-blue); stroke-width: 3.5; stroke-linejoin: round; }
  .guide-row { font-weight: 400; font-size: 30px; fill: var(--ink); }
  .guide-row .label { font-weight: 900; }
  .tick-box { fill: none; stroke: var(--tick-green); stroke-width: 3.5; }
  .tick-mark { fill: none; stroke: var(--tick-green); stroke-width: 5; stroke-linecap: round; stroke-linejoin: round; }
  .sub-bullet { fill: var(--tick-green); }
  .footer-note { font-style: italic; font-weight: 400; font-size: 26px; fill: var(--footer-ink); }
</style>
</head>
<body>
<main class="canvas">
  <svg class="sticker" viewBox="0 0 2156 798" xmlns="http://www.w3.org/2000/svg" role="img" aria-label="Drainwell hot water cylinder maintenance sticker">
    <defs>
      <linearGradient id="warning-fill" x1="0" y1="0" x2="1" y2="0">
        <stop offset="0" stop-color="var(--orange-red)"/>
        <stop offset="0.55" stop-color="var(--orange-mid)"/>
        <stop offset="1" stop-color="var(--orange-yellow)"/>
      </linearGradient>
      <linearGradient id="cta-fill" x1="0" y1="0" x2="1" y2="0">
        <stop offset="0" stop-color="var(--blue-light)"/>
        <stop offset="1" stop-color="var(--blue-deep)"/>
      </linearGradient>
      <g id="tick">
        <rect class="tick-box" x="0" y="-24" width="26" height="26" rx="3"/>
        <path class="tick-mark" d="M5 -12 L13 -3 L30 -28"/>
      </g>
    </defs>

    <rect class="sticker-bg" x="0" y="0" width="2156" height="798"/>

    <!-- Warning panel -->
    <g class="warning-panel">
      <polygon points="1165,0 2156,0 2156,463 975,463" fill="url(#warning-fill)"/>
      <polygon points="1078,207 2156,207 2156,463 975,463" fill="#000" opacity="0.04"/>
      <text class="warning-title" x="1268" y="121">CALL US IMMEDIATELY</text>
      <text class="warning-title" x="1268" y="188">IF YOU NOTICE:</text>
      <text class="warning-item" x="1238" y="247">• No hot water or inconsistent temperature</text>
      <text class="warning-item" x="1238" y="304">• Water leaking from tank or pipes</text>
      <text class="warning-item" x="1238" y="361">• Rust-coloured water</text>
      <text class="warning-item" x="1238" y="417">• Sudden drop in water pressure</text>
    </g>

    <!-- Brand -->
    <g class="brand">
      <circle class="brand-dot" cx="245" cy="150" r="50"/>
      <text class="brand-name" x="312" y="188">DRAINWELL</text>
      <text class="brand-tagline" x="310" y="236">PLUMBING | DRAINAGE | GAS</text>
    </g>

    <!-- Call to action band -->
    <g class="cta-band">
      <polygon points="0,265 1076,265 975,463 0,463" fill="url(#cta-fill)"/>
      <text class="cta-lead" x="65" y="317">NEED HELP FAST? CALL DRAINWELL FIRST!</text>
      <text class="cta-phone" x="60" y="397">PHONE: [0431 258 907]</text>
      <text class="cta-web" x="520" y="446" text-anchor="middle">www.drainwell.com.au</text>
    </g>

    <!-- Maintenance guide -->
    <g class="maintenance-guide">
      <rect class="guide-box" x="65" y="481" width="2027" height="222" rx="14"/>
      <path class="guide-icon" d="M90 504 L90 540 Q105 534 112 540 Q119 534 134 540 L134 504 Q119 498 112 504 Q105 498 90 504 Z M112 504 L112 540"/>
      <text class="guide-title" x="150" y="541">HOT WATER CYLINDER MAINTENANCE</text>

      <use href="#tick" x="98" y="585"/>
      <text class="guide-row" x="150" y="585"><tspan class="label">Monthly:</tspan> Quick visual check for leaks, rust, or pooling water.</text>
      <use href="#tick" x="98" y="631"/>
      <text class="guide-row" x="150" y="631"><tspan class="label">Listen:</tspan> Popping, banging, or rumbling? Could be sediment build-up.</text>
      <use href="#tick" x="98" y="676"/>
      <text class="guide-row" x="150" y="676"><tspan class="label">Annually:</tspan> Book a professional service to check anode, thermostat &amp; valves.</text>

      <use href="#tick" x="1128" y="585"/>
      <text class="guide-row" x="1178" y="585"><tspan class="label">Every 6 Months:</tspan> Test your TPR (Temperature &amp; Pressure Relief) valve.</text>
      <circle class="sub-bullet" cx="1187" cy="621" r="6"/>
      <text class="guide-row" x="1202" y="631">Lift the lever gently until water flows, then release.</text>
      <circle class="sub-bullet" cx="1187" cy="666" r="6"/>
      <text class="guide-row" x="1202" y="676">If it’s blocked or constantly dripping – call us immediately.</text>
    </g>

    <!-- Footer -->
    <g class="footer">
      <text class="footer-note" x="76" y="739">Fully Licensed &amp; Insured | HKTR 62840315 | 24/7 Emergency Service</text>
      <text class="footer-note" x="2080" y="739" text-anchor="end">This guide is for general maintenance only. For all repairs or safety concerns, contact a licensed plumber.</text>
    </g>
  </svg>
</main>
</body>
</html>
```